Psychologist website

Simple psychologist website
Site map:
home
self-test
common conditions
children
contact
about
info

Current website:
http://www.corvalepsychology.com.au/

Not in love with logo, or colours etc - open brief
Happy for new font/style/logo for company name

Customer wants clean, credible and warm and friendly look & feel
stock photos OK

Brief:

One home page - simple with 2 or 3 small areas to tease and attract the user and one template page to suit all the other pages

Pages structurally similar to
http://www.wendlecourt.com.au/
In that the home page is different and the other pages are based on one template

Requirements
Must have
• 2 pages - one home page and one template page
• navigation for site map

```html
<!DOCTYPE html>
<html lang="en">
<head>
<meta charset="utf-8">
<title>Corvale Associates – Clinical Psychologists</title>
<link href="https://fonts.googleapis.com/css2?family=Cantarell&family=Arimo:wght@400&family=Gelasio:wght@500&display=swap" rel="stylesheet">
<style>
  :root{
    --sky-top:#5fa6dc;
    --sky-mid:#a9cdea;
    --mist:#e4ebf0;
    --band:#5b93c2;
    --panel:#f4f6f7;
    --panel-edge:#e3e7ea;
    --ink:#1f2a4a;
    --heading:#6d6d6d;
    --teaser-heading:#8a8a8a;
    --text:#555b60;
    --soft-text:#9aa0a5;
    --link-blue:#8cc5ea;
    --bright-blue:#4db4ea;
    --hero-a:#3f8fd3;
    --hero-b:#7bbde9;
    --rule:#e0e3e6;
    --white:#ffffff;
  }
  *{box-sizing:border-box;margin:0;padding:0}
  html,body{width:1045px;height:1200px;overflow:hidden}
  body{
    position:relative;
    font-family:"Arimo",Arial,sans-serif;
    background:linear-gradient(180deg,var(--sky-top) 0,var(--sky-mid) 420px,var(--mist) 760px,var(--mist) 1104px,var(--band) 1104px,var(--band) 1200px);
  }
  .brand{position:absolute;left:58px;top:30px;display:flex;align-items:flex-start;gap:16px}
  .brand-mark{width:58px;height:54px;border:4px solid var(--ink);border-radius:8px}
  .brand-text{display:flex;flex-direction:column;align-items:flex-end}
  .brand-name{font-family:"Cantarell",sans-serif;font-size:31px;line-height:34px;margin-top:10px;color:var(--ink);white-space:nowrap}
  .brand-tag{font-family:"Cantarell",sans-serif;font-size:15px;line-height:18px;color:var(--white);white-space:nowrap}
  .contact-line{position:absolute;right:56px;top:30px;text-align:right;font-family:"Gelasio",serif;font-weight:500;font-size:21px;line-height:31px;color:var(--white)}

  .panel{position:absolute;left:58px;top:117px;width:930px;height:1014px;background:var(--panel);border-radius:5px;box-shadow:0 1px 4px rgba(0,0,0,.15)}

  .main-nav{position:absolute;left:0;top:0;height:77px;display:flex;font-family:"Cantarell",sans-serif;font-size:14px;color:var(--heading)}
  .main-nav a{display:flex;align-items:center;justify-content:center;height:77px;text-decoration:none;color:inherit;border-right:1px solid var(--panel-edge);padding-bottom:2px}
  .main-nav a:last-child{border-right:none}
  .main-nav .current{color:var(--link-blue)}

  .hero{position:absolute;left:20px;top:65px}
  .hero-title{position:absolute;left:80px;top:130px;font-family:"Cantarell",sans-serif;color:var(--white);line-height:1}
  .hero-title h1{font-weight:400;font-size:35px;letter-spacing:.5px}
  .hero-title p{font-size:27px;color:#b7dcf5;margin-top:6px}

  .teasers{position:absolute;left:41px;top:488px;display:flex}
  .teaser{width:279px}
  .teaser h2{font-family:"Cantarell",sans-serif;font-weight:400;font-size:15.5px;color:var(--teaser-heading)}
  .teaser p{font-size:12.5px;line-height:17px;color:var(--link-blue);margin-top:14px;width:245px}
  .more-link{display:flex;align-items:center;gap:8px;margin-top:13px;font-size:13px;color:var(--text)}
  .more-link svg{flex:none}

  .section-title{font-family:"Cantarell",sans-serif;font-weight:400;font-size:20px;line-height:23px;color:var(--heading)}

  .services{position:absolute;left:24px;top:663px;width:208px}
  .services ul{list-style:none;margin-top:10px}
  .services li{font-size:13.5px;color:var(--text);height:34.5px;line-height:32px;border-bottom:1px solid var(--rule)}
  .services li:last-child{border-bottom:none}

  .vrule{position:absolute;width:1px;background:var(--rule)}

  .welcome{position:absolute;left:283px;top:663px;width:300px}
  .welcome-photo{margin-top:21px;width:294px;height:114px;background:linear-gradient(90deg,#cfd3d0,#b7b6a8 40%,#a7b2a5 70%,#dfe3e6)}
  .welcome p{font-size:11px;line-height:18.5px;color:var(--soft-text);margin-top:14px;width:298px}

  .btn{position:absolute;display:flex;align-items:center;justify-content:center;width:121px;height:37px;border-radius:19px;background:linear-gradient(#f8f8f8,#e6e6e6);box-shadow:0 1px 2px rgba(0,0,0,.18);font-family:"Cantarell",sans-serif;font-size:11.5px;letter-spacing:1px;color:var(--heading)}

  .locations{position:absolute;left:636px;top:668px;width:265px}
  .location{position:relative;padding-left:30px;height:88px}
  .location + .location::before{content:"";position:absolute;left:0;right:0;top:-22px;height:1px;background:var(--rule)}
  .location svg{position:absolute;left:0;top:0}
  .location h3{font-family:"Cantarell",sans-serif;font-weight:400;font-size:16px;line-height:19px;color:var(--bright-blue)}
  .location p{font-size:10.5px;line-height:17px;color:var(--soft-text);margin-top:8px;width:215px}

  .site-footer{position:absolute;left:58px;top:1158px;width:930px;display:flex;justify-content:space-between;font-family:"Cantarell",sans-serif;font-size:12.5px;color:var(--white)}
  .site-footer nav{display:flex}
  .site-footer span,.site-footer nav a{padding:0 10px;border-left:1px solid rgba(255,255,255,.8);color:inherit;text-decoration:none}
  .site-footer .first{border-left:none;padding-left:0}
  .site-footer nav a:last-child{padding-right:2px}
</style>
</head>
<body>
  <header>
    <div class="brand">
      <div class="brand-mark"></div>
      <div class="brand-text">
        <div class="brand-name">Corvale Associates</div>
        <div class="brand-tag">Clinical Psychologists</div>
      </div>
    </div>
    <div class="contact-line">Phone: 95240318<br>for all appointments and enquiries</div>
  </header>

  <main class="panel">
    <nav class="main-nav">
      <a class="current" style="width:95px">HOME</a>
      <a style="width:125px">ABOUT US</a>
      <a style="width:121px">SELF-TEST</a>
      <a style="width:214px">COMMON CONDITIONS</a>
      <a style="width:124px">CHILDREN</a>
      <a style="width:88px">INFO</a>
      <a style="width:163px">CONTACTS US</a>
    </nav>

    <svg class="hero" width="890" height="600" viewBox="0 0 890 600">
      <defs>
        <linearGradient id="heroSky" x1="0" y1="0" x2="0" y2="1">
          <stop offset="0" stop-color="var(--hero-a)"/>
          <stop offset="1" stop-color="var(--hero-b)"/>
        </linearGradient>
        <linearGradient id="lowerPanel" x1="0" y1="0" x2="0" y2="1">
          <stop offset="0" stop-color="#e9edf0"/>
          <stop offset=".35" stop-color="#f7f8f9"/>
          <stop offset="1" stop-color="#f1f3f5"/>
        </linearGradient>
      </defs>
      <path d="M0 6 Q445 -2 890 6 L890 575 Q445 541 0 575 Z" fill="url(#lowerPanel)" stroke="#e4e7ea"/>
      <path d="M8 18 Q445 42 882 18 L882 280 Q445 460 8 280 Z" fill="url(#heroSky)" stroke="var(--white)" stroke-width="4" role="img" aria-label="Stock photo of a smiling woman with arms spread wide against a clear blue sky"/>
    </svg>
    <div class="hero-title">
      <h1>LOREM IPSUM</h1>
      <p>MORBI LUCTUS ALIQUAM</p>
    </div>

    <section class="teasers">
      <article class="teaser">
        <h2>CLINICAL PSYCHOLOGY</h2>
        <p>Etgisriea jesertas leraen onsertas ersasera rurugiat masidabi nunc.</p>
        <div class="more-link"><svg width="16" height="16" viewBox="0 0 16 16"><circle cx="8" cy="8" r="7" fill="none" stroke="#b4b8bb"/><path d="M6.5 5 L10 8 L6.5 11 Z" fill="#9a9ea2"/></svg>Read More</div>
      </article>
      <article class="teaser">
        <h2>PARENT–CHILD THERAPY</h2>
        <p>Nadgravida staseras sus necase kertyad aseluctus ascenas tristiquorc.</p>
        <div class="more-link"><svg width="16" height="16" viewBox="0 0 16 16"><circle cx="8" cy="8" r="7" fill="none" stroke="#b4b8bb"/><path d="M6.5 5 L10 8 L6.5 11 Z" fill="#9a9ea2"/></svg>Read More</div>
      </article>
      <article class="teaser">
        <h2>ANXIETY DISORDERS</h2>
        <p>Arestertaseras cursus necase kertyad aseluctus ascenas tristiquorc.</p>
        <div class="more-link"><svg width="16" height="16" viewBox="0 0 16 16"><circle cx="8" cy="8" r="7" fill="none" stroke="#b4b8bb"/><path d="M6.5 5 L10 8 L6.5 11 Z" fill="#9a9ea2"/></svg>Read More</div>
      </article>
    </section>

    <section class="services">
      <h2 class="section-title">OUR SERVICES</h2>
      <ul>
        <li>Psychometric Assessment</li>
        <li>Mood</li>
        <li>Trauma</li>
        <li>Addictions</li>
        <li>Physical Health</li>
        <li>Infant and child services</li>
        <li>Skills to Enhance your life</li>
      </ul>
    </section>

    <div class="vrule" style="left:255px;top:702px;height:243px"></div>

    <section class="welcome">
      <h2 class="section-title">WELCOME CORVALE</h2>
      <div class="welcome-photo" role="img" aria-label="Stock photo of a smiling family of three in a home library"></div>
      <p>Our psychologists provide a comfortable, supportive, and confidential environment for their clients. Our first goal is for you to feel comfortable in exploring issues and sharing sharing your concerns</p>
    </section>
    <div class="btn" style="left:284px;top:930px">READ MORE</div>

    <div class="vrule" style="left:612px;top:662px;height:318px"></div>

    <section class="locations">
      <article class="location">
        <svg width="18" height="18" viewBox="0 0 18 18"><circle cx="9" cy="9" r="8.5" fill="#dbeaf5"/><circle cx="9" cy="9" r="6" fill="var(--bright-blue)"/><path d="M7.5 6 L10.5 9 L7.5 12" fill="none" stroke="#fff" stroke-width="1.5"/></svg>
        <h3>SYDNEY CBD</h3>
        <p>Bertase dolor sit amet conectu edipiscing onmyhe ndrerit mauris ketyade.</p>
      </article>
      <article class="location">
        <svg width="18" height="18" viewBox="0 0 18 18"><circle cx="9" cy="9" r="8.5" fill="#dbeaf5"/><circle cx="9" cy="9" r="6" fill="var(--bright-blue)"/><path d="M7.5 6 L10.5 9 L7.5 12" fill="none" stroke="#fff" stroke-width="1.5"/></svg>
        <h3>CHATSWOOD</h3>
        <p>Bertase conectu eradipiscing dolor sit ondrerit mauris ketyade</p>
      </article>
      <article class="location">
        <svg width="18" height="18" viewBox="0 0 18 18"><circle cx="9" cy="9" r="8.5" fill="#dbeaf5"/><circle cx="9" cy="9" r="6" fill="var(--bright-blue)"/><path d="M7.5 6 L10.5 9 L7.5 12" fill="none" stroke="#fff" stroke-width="1.5"/></svg>
        <h3>WESTMEAD</h3>
        <p>Dolor sit amet conectu eradipiscing kety Phasellus porce suscipit.</p>
      </article>
    </section>
    <div class="btn" style="left:666px;top:933px">READ MORE</div>
  </main>

  <footer class="site-footer">
    <div><span class="first">© 2013 Corvale Psychology</span><span>Privacy policy</span></div>
    <nav>
      <a class="first">Home</a><a>About Us</a><a>Self-Test</a><a>Common Conditions</a><a>Children</a><a>Info</a><a>contact</a>
    </nav>
  </footer>
</body>
</html>
```